A WEBSITE FOR A JEWELLERY RETAIL STORE WITH A SHOPPING CART, AND ABILITY TO ORDER ONLINE.

I require a website with a shopping cart.

We sell MAINLY diamond jewellery (such as rings etc). I need it to be simple to change prices with only a few buttons, as the price fluctuates due to the US Dollar.

We are a diamond wholesaler, selling directly to the public, so we guarantee the lowest prices in Australia.

There is also a link to current inventory that will need to be uploaded to the site.

This could be an ongoing job, where you will be paid weekly to maintain and update the website if you wish.

Target Market(s)

People getting engaged, and wanting to buy a diamond ring.

Number of Pages Required

5+ page

Colors

Designer to choose colors to be used in the design.

Requirements
Must have
• elegant.
• modern.
• professional.
• SHOPPING CART.
• ABILITY TO SEARCH FOR LOOSE DIAMONDS (LINK THAT NEEDS TO BE EMBEDDED WILL BE SENT WHICH SHOWS CURRENT STOCK).
• ENGAGEMENT RINGS
• WEDDING RINGS
• DIAMOND EARRINGS
• DIAMOND PENDANTS
• LOOSE DIAMONDS.
• SALE ITEMS.
• OTHER JEWELLERY.
• EDUCATION
• WISH LIST
• CART.
Nice to have
• a good place to look for inspiration on pages is https://www.lumenvael.example.
• YOU MAY VISIT OUR FACETOME PAGE AT.
• HTTP://WWW.SOCIALPAGE.EXAMPLE/QUILLSTONEJEWELLERS
Should not have
• We don't want it too busy.

```html
<!DOCTYPE html>
<html lang="en">
<head>
<meta charset="utf-8">
<title>Quillstone Jewellers – Wholesale Diamond Jewellery</title>
<link rel="stylesheet" href="https://fonts.googleapis.com/css2?family=Poppins:wght@400;500;600;700&display=swap">
<style>
:root{
  --red:#ed1c24;
  --red-soft:#f04f55;
  --ink:#111111;
  --dark:#1b1b1b;
  --grey:#777777;
  --line:#e2e2e2;
  --star:#f6b91a;
  --white:#ffffff;
}
*{box-sizing:border-box;margin:0;padding:0}
html,body{width:1200px;height:3586px;overflow:hidden}
body{font-family:'Poppins',sans-serif;color:var(--ink);background:var(--white);position:relative}
.abs{position:absolute}
a{color:inherit;text-decoration:none}

/* top bar */
.topbar{top:0;left:0;width:1200px;height:50px;font-size:12px;font-weight:500}
.topbar .offer{left:157px;top:16px}
.topbar .lang{left:842px;top:16px;display:flex;align-items:center;gap:6px}
.topbar .lang i{display:inline-block;width:18px;height:11px;background:linear-gradient(#c8102e 0 33%,#fff 33% 66%,#1e3a8a 66%)}
.topbar .curr{left:975px;top:16px}

/* header */
.brand{display:flex;align-items:center;gap:10px;font-weight:600;color:var(--ink)}
.brand .mark{width:30px;height:30px;background:var(--ink)}
.brand .name{font-size:17px;line-height:1.05;letter-spacing:1px}
.header-brand{left:152px;top:68px}
.search{left:433px;top:75px;width:340px;height:38px;border:1.5px solid var(--red);display:flex}
.search span{flex:1;font-size:12px;color:var(--grey);padding:10px 12px}
.search b{width:48px;background:var(--red);display:flex;align-items:center;justify-content:center}
.user{left:893px;top:78px}
.cart{left:948px;top:76px;display:flex;align-items:center;gap:10px;font-weight:600;font-size:15px}

/* nav */
.nav{top:145px;left:0;width:1200px;height:68px;background:var(--red)}
.dept{left:139px;top:0;width:244px;height:68px;background:var(--dark);color:#fff;font-size:15px;font-weight:600;display:flex;align-items:center;justify-content:space-between;padding:0 18px}
.nav ul{list-style:none;position:absolute;left:425px;top:23px;display:flex;gap:44px;color:#fff;font-size:15px;font-weight:500}

/* hero */
.hero{top:213px;left:0;width:1200px;height:567px;background:#000}
.hero .photo{left:0;top:0;width:590px;height:567px;background:radial-gradient(ellipse at 45% 45%,#d79a12 0,#8a6a2a 18%,#3a3a3a 38%,#0b0b0b 70%)}
.hero h1{left:595px;top:170px;color:#fff;font-size:33px;font-weight:700;line-height:1.45;width:520px}
.hero p{left:598px;top:287px;color:#fff;font-size:15px}
.btn{background:var(--red);color:#fff;font-weight:500;display:flex;align-items:center;justify-content:center}
.hero .btn{left:598px;top:351px;width:150px;height:53px;font-size:15px}

/* promo */
.promo{top:810px;width:446px;height:227px;background:linear-gradient(135deg,#2c2c2c,#0d0d0d)}
.promo small{position:absolute;left:32px;top:62px;color:#fff;font-size:12px}
.promo h3{position:absolute;left:32px;top:100px;color:#fff;font-size:23px;font-weight:700;line-height:1.3}
.promo .ring{position:absolute;right:30px;top:30px;width:170px;height:170px;border-radius:50%;background:radial-gradient(circle,#e8e8e8 0,#9a9a9a 35%,rgba(0,0,0,0) 70%)}

/* services */
.services{left:139px;top:1076px;width:236px;height:442px;background:var(--red-soft);border-radius:10px;color:#fff}
.svc{position:absolute;left:18px;display:flex;gap:14px}
.svc .ic{width:44px;height:44px;flex:none}
.svc h4{font-size:14px;font-weight:600;margin-top:2px}
.svc p{font-size:10px;line-height:1.9;width:120px}

/* deal */
.deal-title{left:420px;top:1098px;font-size:16px;font-weight:600}
.deal-nav{left:947px;top:1104px;font-size:10px;color:var(--grey)}
.deal-nav b{color:var(--ink);font-weight:500;margin-left:16px}
.deal{left:400px;top:1138px;width:657px;height:362px;border:2px solid var(--line);border-radius:14px;box-shadow:0 2px 6px rgba(0,0,0,.08)}
.deal .pic{position:absolute;left:19px;top:24px;width:246px;height:300px;border:2px solid var(--line);border-radius:14px}
.deal .off{position:absolute;left:200px;top:38px;color:var(--red);font-size:14px;font-weight:600}
.deal h5{position:absolute;left:290px;top:56px;font-size:15px;font-weight:500}
.deal .stars{position:absolute;left:290px;top:84px;font-size:26px}
.deal .price{position:absolute;left:290px;top:124px}
.deal .desc{position:absolute;left:290px;top:158px;width:350px;font-size:10px;line-height:2.1}
.timer{position:absolute;left:290px;top:236px;display:flex;gap:8px}
.timer div{width:52px;text-align:center}
.timer b{display:flex;align-items:center;justify-content:center;height:60px;background:var(--ink);color:#fff;font-size:30px;font-weight:600}
.timer span{display:block;font-size:9px;color:var(--grey);margin-top:8px}

.stars{color:var(--star);letter-spacing:2px}
.price{font-size:14px;font-weight:600;color:var(--red)}
.price s{color:var(--grey);font-weight:400;margin-left:8px;font-size:13px}

/* sections */
.tabs{left:142px;top:1562px;display:flex;gap:45px;font-size:23px;font-weight:600}
.tabs .active{color:var(--red)}
.arrows{display:flex;gap:30px}
.grid{left:139px;display:flex;gap:26px}
.card{width:216px;height:323px;border:2px solid var(--line);border-radius:14px;position:relative;background:#fff;box-shadow:0 2px 5px rgba(0,0,0,.06)}
.card .pic{position:absolute;left:28px;top:48px;width:160px;height:150px;border-radius:50%;background:radial-gradient(circle,#f4f4f4 0,#d6d6d6 38%,#fff 70%)}
.card .pic.gold{background:radial-gradient(circle,#f4f4f4 0,#d8c49a 38%,#fff 70%)}
.card .badge{position:absolute;right:14px;top:18px;color:var(--red);font-size:14px;font-weight:600}
.card h6{position:absolute;left:10px;top:216px;font-size:15px;font-weight:400}
.card .stars{position:absolute;left:10px;top:242px;font-size:25px}
.card .price{position:absolute;left:10px;top:286px}

.queen{left:139px;top:1991px;width:920px;height:378px;background:linear-gradient(100deg,#5a1a22 0,#7a1e28 35%,#3a1216 70%,#1f0a0c 100%)}
.queen small{position:absolute;left:225px;top:78px;color:#fff;font-size:14px}
.queen h3{position:absolute;left:225px;top:120px;color:#fff;font-size:32px;font-weight:700;line-height:1.25}
.queen .btn{left:225px;top:216px;width:107px;height:38px;font-size:12px}

.feat-title{left:142px;top:2398px;font-size:23px;font-weight:600;color:var(--red)}

.quality{left:218px;top:2827px;width:368px;height:237px;background:linear-gradient(135deg,#4a4a4a,#1e1e1e);color:#fff;text-align:center}
.quality h4{margin-top:20px;font-size:18px;font-weight:600}
.quality p{font-size:11px;line-height:1.75;padding:10px 26px 0}
.quality .btn,.edu .btn{position:absolute;left:134px;top:190px;width:100px;height:36px;font-size:11px}
.edu{left:612px;top:2827px;width:368px;height:237px;border:2px solid var(--line);border-radius:6px}
.edu h4{text-align:center;color:var(--red);font-size:19px;font-weight:600;margin-top:18px}
.edu p{font-size:11px;line-height:1.8;padding:14px 24px 0}
.edu ul{list-style:none;position:absolute;left:40px;top:120px;width:300px;display:grid;grid-template-columns:1fr 1fr;row-gap:20px;font-size:11px}

.news{top:3097px;left:0;width:1200px;height:91px;background:var(--red);color:#fff}
.news .ic{left:164px;top:22px}
.news h4{left:239px;top:20px;font-size:19px;font-weight:600}
.news p{left:239px;top:52px;font-size:12px}
.news .field{left:597px;top:30px;width:318px;height:38px;background:#fff;color:var(--ink);font-size:12px;padding:11px 12px}
.news .sub{left:922px;top:30px;width:107px;height:38px;background:var(--dark);font-size:15px;font-weight:600;display:flex;align-items:center;justify-content:center}

.footer{top:3188px;left:0;width:1200px;height:306px;background:var(--dark);color:#fff}
.footer h4{font-size:23px;font-weight:600;position:absolute}
.footer .links{left:144px;top:112px;display:flex;gap:30px;font-size:12px}
.footer .social{left:144px;top:228px;display:flex;gap:22px;font-size:13px;align-items:center}
.footer .social span{display:flex;gap:6px;align-items:center}
.footer .social i{width:15px;height:15px;background:#fff;display:inline-block}
.footer .say{left:729px;top:55px;font-size:16px}
.footer .quote{left:729px;top:95px;width:340px;font-size:11px;line-height:2.25}
.footer .who{left:729px;top:204px;color:var(--red);font-size:20px;font-weight:600}
.footer .role{left:729px;top:236px;font-size:11px}
.dots{left:729px;top:258px;display:flex;gap:6px}
.dots i{width:9px;height:9px;border-radius:50%;background:#777}
.dots i:first-child{background:var(--red)}

.bottom{top:3494px;left:0;width:1200px;height:92px}
.bottom .copy{left:139px;top:40px;font-size:12px}
.bottom-brand{left:520px;top:28px}
.pay{left:748px;top:30px;display:flex;gap:10px}
.pay i{width:38px;height:28px;border-radius:4px;display:block}
</style>
</head>
<body>

<div class="abs topbar">
  <span class="abs offer">Get Special 27% Discount On Items</span>
  <span class="abs lang"><i></i>Language ▾</span>
  <span class="abs curr">$ Currency ▾</span>
</div>

<a class="abs brand header-brand" href="#"><span class="mark"></span><span class="name">QUILLSTONE<br>JEWELLERS</span></a>
<div class="abs search"><span>Search Product Here...</span><b><svg width="20" height="20" viewBox="0 0 20 20" fill="none" stroke="#fff" stroke-width="2.2"><circle cx="8.5" cy="8.5" r="6"/><path d="M13 13l5 5"/></svg></b></div>
<svg class="abs user" width="34" height="36" viewBox="0 0 34 36" fill="#111"><circle cx="17" cy="10" r="8"/><path d="M2 36c0-10 6-15 15-15s15 5 15 15z"/></svg>
<div class="abs cart"><svg width="40" height="36" viewBox="0 0 40 36" fill="none" stroke="#111" stroke-width="3"><path d="M2 4h6l5 20h20l4-14H11"/><circle cx="15" cy="31" r="3" fill="#111"/><circle cx="30" cy="31" r="3" fill="#111"/></svg>Cart</div>

<nav class="abs nav">
  <div class="abs dept">All Departments<svg width="14" height="9" viewBox="0 0 14 9" fill="none" stroke="#fff" stroke-width="2"><path d="M1 8l6-6 6 6"/></svg></div>
  <ul><li>Home</li><li>About Us</li><li>Shop</li><li>Blog</li><li>Contact</li></ul>
</nav>

<section class="abs hero">
  <div class="abs photo" role="img" aria-label="Close-up of a diamond ring with a large yellow gemstone on black"></div>
  <h1 class="abs">WHOLESALE PRICES- DIRECT<br>TO THE PUBLIC</h1>
  <p class="abs">Guaranteed Lowest prices in Australia.</p>
  <a class="abs btn" href="#">SHOP NOW</a>
</section>

<div class="abs promo" style="left:139px"><small>Most Popular Jewellery</small><h3>Latest Diamond<br>Ring</h3><div class="ring" role="img" aria-label="Marquise diamond ring"></div></div>
<div class="abs promo" style="left:612px"><small>Most Popular Jewellery</small><h3>Latest Diamond<br>Ring</h3><div class="ring" role="img" aria-label="Cushion cut diamond ring with gold band"></div></div>

<aside class="abs services">
  <div class="svc" style="top:22px"><svg class="ic" viewBox="0 0 44 44" fill="none" stroke="#fff" stroke-width="2.4"><path d="M6 26h32l-4 10H10z"/><path d="M12 26V14h20v12M22 6v8"/></svg><div><h4>Free Shipping</h4><p>Delivery All Over The World Free</p></div></div>
  <div class="svc" style="top:122px"><svg class="ic" viewBox="0 0 44 44" fill="none" stroke="#fff" stroke-width="2.4"><circle cx="22" cy="16" r="9"/><path d="M8 40c2-9 8-13 14-13s12 4 14 13M10 16h-2v6h3M34 16h2v6h-3"/></svg><div><h4>24/7 Online Help</h4><p>Support Customer 24 Hours Helps</p></div></div>
  <div class="svc" style="top:222px"><svg class="ic" viewBox="0 0 44 44" fill="none" stroke="#fff" stroke-width="2.4"><ellipse cx="22" cy="25" rx="15" ry="11"/><path d="M18 14l4-6 4 6M22 20v10"/></svg><div><h4>Money Return</h4><p>Delivery All Over The World Free</p></div></div>
  <div class="svc" style="top:322px"><svg class="ic" viewBox="0 0 44 44" fill="none" stroke="#fff" stroke-width="2.4"><path d="M22 4l5 4 6-1 1 6 5 4-3 5 2 6-6 2-2 6-6-2-5 4-4-5-6-1 1-6-4-5 5-4-1-6 6 1z"/><path d="M16 28l12-12"/><circle cx="17" cy="17" r="2"/><circle cx="27" cy="27" r="2"/></svg><div><h4>User Discount</h4><p>Delivery All Over The World Free</p></div></div>
</aside>

<h2 class="abs deal-title">Deal of The Week</h2>
<div class="abs deal-nav">Previous<b>Next</b></div>
<div class="abs deal">
  <div class="pic" role="img" aria-label="Halo diamond engagement ring"></div>
  <span class="off">8% OFF</span>
  <h5>Ipsam voluptatem quia voluptas</h5>
  <div class="stars">★★★★★</div>
  <div class="price">$110.00<s>$119.00</s></div>
  <p class="desc">Sed ut perspiciatis unde omnis iste natus error sit voluptatem accusantium doloremque laudantium, totam rem aperiam, eaque ipsa quae ab illo inventore veritatis et quasi.</p>
  <div class="timer"><div><b>2</b><span>Days</span></div><div><b>05</b><span>Hours</span></div><div><b>20</b><span>Mins</span></div><div><b>15</b><span>Sec</span></div></div>
</div>

<div class="abs tabs"><span class="active">New Arrival</span><span>Best Seller</span></div>
<div class="abs arrows" style="left:988px;top:1574px"><svg width="12" height="16" viewBox="0 0 12 16" fill="none" stroke="#111" stroke-width="2.5"><path d="M9 2L3 8l6 6"/></svg><svg width="12" height="16" viewBox="0 0 12 16" fill="none" stroke="#111" stroke-width="2.5"><path d="M3 2l6 6-6 6"/></svg></div>

<div class="abs grid" style="top:1630px">
  <div class="card"><span class="badge">13 % off</span><div class="pic gold" role="img" aria-label="Diamond ring with gold band"></div><h6>Ipsam voluptatem</h6><div class="stars">★★★★★</div><div class="price">$110.00<s>$119.00</s></div></div>
  <div class="card"><div class="pic" role="img" aria-label="Halo diamond ring"></div><h6>Ipsam voluptatem</h6><div class="stars">★★★★★</div><div class="price">$110.00<s>$119.00</s></div></div>
  <div class="card"><div class="pic" role="img" aria-label="Oval diamond ring"></div><h6>Ipsam voluptatem</h6><div class="stars">★★★★★</div><div class="price">$110.00<s>$119.00</s></div></div>
  <div class="card"><div class="pic gold" role="img" aria-label="Diamond ring with gold band"></div><h6>Ipsam voluptatem</h6><div class="stars">★★★★★</div><div class="price">$110.00<s>$119.00</s></div></div>
</div>

<section class="abs queen" role="img" aria-label="Woman admiring a ring box against soft red lights">
  <small>Most Popular Rings</small>
  <h3>Modern Queen<br>Ring</h3>
  <a class="abs btn" href="#">SHOP NOW</a>
</section>

<h2 class="abs feat-title">Featured Product</h2>
<div class="abs arrows" style="left:988px;top:2410px"><svg width="12" height="16" viewBox="0 0 12 16" fill="none" stroke="#111" stroke-width="2.5"><path d="M9 2L3 8l6 6"/></svg><svg width="12" height="16" viewBox="0 0 12 16" fill="none" stroke="#111" stroke-width="2.5"><path d="M3 2l6 6-6 6"/></svg></div>

<div class="abs grid" style="top:2464px">
  <div class="card"><span class="badge">13 % off</span><div class="pic gold" role="img" aria-label="Diamond ring with gold band"></div><h6>Ipsam voluptatem</h6><div class="stars">★★★★★</div><div class="price">$110.00<s>$119.00</s></div></div>
  <div class="card"><div class="pic" role="img" aria-label="Halo diamond ring"></div><h6>Ipsam voluptatem</h6><div class="stars">★★★★★</div><div class="price">$110.00<s>$119.00</s></div></div>
  <div class="card"><div class="pic" role="img" aria-label="Oval diamond ring"></div><h6>Ipsam voluptatem</h6><div class="stars">★★★★★</div><div class="price">$110.00<s>$119.00</s></div></div>
  <div class="card"><div class="pic gold" role="img" aria-label="Diamond ring with gold band"></div><h6>Ipsam voluptatem</h6><div class="stars">★★★★★</div><div class="price">$110.00<s>$119.00</s></div></div>
</div>

<div class="abs quality" role="img" aria-label="Couple in a jewellery store, darkened">
  <h4>Above and Beyond Quality</h4>
  <p>Are you tired of stunning, but flimsy pieces? Beauty may be in the eye of the beholder, but quality should never be a compromise. No matter what type of jewelry you're looking for, we guarantee durability. We design well-built jewelry so you can focus on looking good.</p>
  <a class="abs btn" href="#">READ MORE</a>
</div>
<div class="abs edu">
  <h4>Diamond Education</h4>
  <p>Learn about the "four C's" to help you with your online diamond shopping:</p>
  <ul><li>Diamond Cut</li><li>Diamond Color</li><li>Diamond Clarity</li><li>Carat Weight</li></ul>
  <a class="abs btn" href="#">READ MORE</a>
</div>

<section class="abs news">
  <svg class="abs ic" width="56" height="46" viewBox="0 0 56 46" fill="none" stroke="#fff" stroke-width="2.5"><path d="M4 18l24-15 24 15v25H4z"/><path d="M4 18l24 16 24-16"/><path d="M14 12h28v14"/></svg>
  <h4 class="abs">NEWSLETTER</h4>
  <p class="abs">Signup Our Newsletter And get latest updates!</p>
  <div class="abs field">Your Email Address</div>
  <div class="abs sub">Subscribe</div>
</section>

<footer class="abs footer">
  <h4 style="left:144px;top:50px">Information</h4>
  <div class="abs links"><span>About Us</span><span>Delivery Information</span><span>Privacy Policy</span><span>Terms &amp; Conditions</span><span>Site Map</span></div>
  <h4 style="left:144px;top:170px">Follow On Social</h4>
  <div class="abs social"><span><i></i>Facetome</span><span><i></i>LinkNest</span><span><i></i>ViewTube</span><span><i></i>Snapgram</span><span><i></i>Pinboardly</span></div>
  <h4 class="say" style="font-size:16px">What They Says</h4>
  <p class="abs quote">Sed ut perspiciatis unde omnis iste natus error sit voluptatem accusantium doloremque laudantium, totam rem aperiam, eaque ipsa quae ab illo inventore veritatis et quasi architecto beatae vitae dicta sunt explicabo.</p>
  <div class="abs who">Elena Marsh</div>
  <div class="abs role">Customer</div>
  <div class="abs dots"><i></i><i></i><i></i></div>
</footer>

<div class="abs bottom">
  <span class="abs copy">Copyright © 2018 Quillstone Jewellers - All Rights Reserved.</span>
  <span class="abs brand bottom-brand"><span class="mark"></span><span class="name">QUILLSTONE<br>JEWELLERS</span></span>
  <div class="abs pay"><i style="background:#1f3b73"></i><i style="background:#e7e7e7"></i><i style="background:#222"></i><i style="background:#1a4fa0"></i><i style="background:#3a8fd8"></i><i style="background:#e6e6e6"></i></div>
</div>

</body>
</html>
```